Financial Advisor / Asset Manager Zup Design

I'm currently hosting with Zup and my first attempt at a website is live at www.ravenholtwealth.example Clearly I am not a web designer and I need help making this more catchy, modern, cross-platform compatible, search engine optimized, etc. I've got logos, hex color pallets, and a slew of other graphics. I'm interested in working with a winning designer to write/refine my copy/language to complete the build.

Full set of graphics https://pics.lumora-share.example/q71TzR05KwPd2MhXN do NOT use the CONSULTING graphics as this is for a related business / different website

Target Market(s)

Individuals, small institutions, endowments, non-profits seeking financial advice and asset / portfolio management

Industry/Entity Type

Financial Services

Coding

Coded - Design and coding required

Font styles to use
Other font styles liked:
• AvenirLTStd - Black, Book, and Roman as appropriate

Requirements
Must have
• Complete, cross platform website integrating my existing logo
Nice to have
• Easy to update format for go-forward maintenance

```html
<!DOCTYPE html>
<html lang="en">
<head>
<meta charset="utf-8">
<title>Ravenholt Wealth — Professional Management</title>
<link rel="stylesheet" href="https://fonts.googleapis.com/css2?family=Nunito+Sans:wght@400;600;700;800&display=swap">
<style>
  :root {
    --brand-blue: #0a55a8;
    --ink: #111111;
    --white: #ffffff;
    --page-grey: #f1f1f1;
    --sky-deep: #1f3f7a;
    --sky-mid: #4a6fa8;
    --forest: #4b5a22;
    --lake: #2c4f96;
  }
  * { box-sizing: border-box; margin: 0; padding: 0; }
  html, body { width: 1200px; height: 1000px; overflow: hidden; }
  body {
    font-family: "Nunito Sans", "Avenir", sans-serif;
    background: var(--page-grey);
    position: relative;
  }
  .hero {
    position: absolute; inset: 0 0 auto 0; height: 590px;
    clip-path: polygon(0 0, 1200px 0, 1200px 585px, 0 510px);
  }
  .hero-photo {
    position: absolute; inset: 0;
    background:
      linear-gradient(180deg, rgba(20,30,50,.55) 0, rgba(20,30,50,0) 90px),
      linear-gradient(180deg, var(--sky-deep) 0%, #6b7fa3 18%, #dfe6ef 26%, #5b6e8c 34%, var(--forest) 44%, #2d3a1c 50%, var(--lake) 62%, #8fa6cf 78%, var(--lake) 100%);
  }
  .site-header { position: absolute; top: 0; left: 0; right: 0; height: 80px; color: var(--white); }
  .brand {
    position: absolute; left: 168px; top: 24px;
    display: flex; align-items: center; gap: 8px;
    font-size: 17px; font-weight: 700; letter-spacing: .5px;
  }
  .brand-dot { width: 12px; height: 12px; border-radius: 50%; background: var(--white); }
  .main-nav { position: absolute; top: 31px; left: 490px; display: flex; font-size: 14px; }
  .main-nav a { color: var(--white); text-decoration: none; margin-right: 56px; }
  .main-nav a.is-active { font-weight: 700; }
  .header-tools { position: absolute; left: 968px; top: 28px; display: flex; gap: 20px; }
  .cart-count { position: absolute; left: 58px; top: -3px; font-size: 10px; }
  .hero-copy {
    position: absolute; top: 230px; left: 0; right: 0; text-align: center; color: var(--white);
    text-shadow: 0 1px 6px rgba(0,0,0,.3);
  }
  .hero-kicker { font-size: 16px; font-weight: 600; letter-spacing: .3px; }
  .hero-title { font-size: 50px; font-weight: 800; line-height: 57px; margin-top: 2px; }
  .services-backdrop {
    position: absolute; left: 409px; top: 560px; right: 0; bottom: 0;
    background: linear-gradient(180deg, #e6e8ea 0%, #f4f4f4 45%, #eeeeee 100%);
    opacity: .8;
  }
  .services-panel {
    position: absolute; left: 0; top: 615px; width: 409px; height: 385px;
    background: var(--brand-blue);
  }
  .services-title {
    position: absolute; left: 54px; top: 684px;
    font-size: 40px; font-weight: 700; color: var(--white);
  }
  .carousel-controls { position: absolute; left: 1058px; top: 698px; display: flex; gap: 30px; }
  .service-cards { position: absolute; left: 58px; top: 768px; display: flex; }
  .service-card {
    position: relative; width: 270px; height: 240px; color: var(--white);
    border-right: 1px solid rgba(255,255,255,.5);
  }
  .service-photo { position: absolute; inset: 0; }
  .card-1 .service-photo { background: linear-gradient(180deg, #a9c3dc 0%, #8d8b86 25%, #6f7a5e 60%, #2f3a2e 100%); }
  .card-2 .service-photo { background: linear-gradient(180deg, #3f78c8 0%, #c9d3de 30%, #6f7d8a 60%, #2b3735 100%); }
  .card-3 .service-photo { background: linear-gradient(180deg, #c6ccd0 0%, #6c6f6c 30%, #c9d2d4 50%, #4d5a55 75%, #2a3430 100%); }
  .card-4 .service-photo { background: linear-gradient(180deg, #3a5a8c 0%, #b8c7d6 15%, #6d86a3 30%, #7d5f53 60%, #3b3030 100%); }
  .service-text { position: absolute; left: 13px; top: 178px; width: 200px; }
  .service-name { font-size: 17px; font-weight: 600; }
  .service-desc { font-size: 13px; line-height: 14px; margin-top: 5px; }
  .service-arrow { position: absolute; left: 239px; top: 212px; }
</style>
</head>
<body>
  <section class="hero">
    <div class="hero-photo" role="img" aria-label="Snow-capped mountains reflected in a calm forest lake"></div>
    <header class="site-header">
      <div class="brand"><span class="brand-dot"></span>RAVENHOLT WEALTH</div>
      <nav class="main-nav">
        <a href="#" class="is-active">Home</a>
        <a href="#">About</a>
        <a href="#">FAQs</a>
        <a href="#">Services</a>
        <a href="#">Contact</a>
      </nav>
      <div class="header-tools">
        <svg width="18" height="18" viewBox="0 0 18 18" aria-label="Search"><circle cx="7" cy="7" r="5.5" fill="none" stroke="#fff" stroke-width="2"/><line x1="11" y1="11" x2="16" y2="16" stroke="#fff" stroke-width="2"/></svg>
        <svg width="18" height="21" viewBox="0 0 18 21" aria-label="Cart"><path d="M2 7h14v13H2z" fill="none" stroke="#fff" stroke-width="1.8"/><path d="M5.5 7V5a3.5 3.5 0 0 1 7 0v2" fill="none" stroke="#fff" stroke-width="1.8"/></svg>
        <span class="cart-count">0</span>
      </div>
    </header>
    <div class="hero-copy">
      <p class="hero-kicker">PROFESSIONAL MANAGEMENT</p>
      <h1 class="hero-title">TO MAKE YOUR MONEY<br>WORK FOR YOU</h1>
    </div>
  </section>

  <div class="services-backdrop" role="img" aria-label="Faint misty mountain range"></div>
  <div class="services-panel"></div>
  <h2 class="services-title">Our Services</h2>
  <div class="carousel-controls">
    <svg width="20" height="26" viewBox="0 0 20 26" aria-label="Previous"><polyline points="14,2 4,13 14,24" fill="none" stroke="#0a55a8" stroke-width="2"/></svg>
    <svg width="20" height="26" viewBox="0 0 20 26" aria-label="Next"><polyline points="6,2 16,13 6,24" fill="none" stroke="#111" stroke-width="2"/></svg>
  </div>

  <div class="service-cards">
    <article class="service-card card-1">
      <div class="service-photo" role="img" aria-label="Alpine peaks above a green valley"></div>
      <div class="service-text"><h3 class="service-name">You Come First</h3><p class="service-desc">We always act in the best interests of our clients</p></div>
      <svg class="service-arrow" width="18" height="16" viewBox="0 0 18 16"><path d="M1 8h15M10 2l6 6-6 6" fill="none" stroke="#fff" stroke-width="2"/></svg>
    </article>
    <article class="service-card card-2">
      <div class="service-photo" role="img" aria-label="Clouds over a mountain valley"></div>
      <div class="service-text"><h3 class="service-name">Personalized Services</h3><p class="service-desc">We get to know you in order to service your unique needs</p></div>
      <svg class="service-arrow" width="18" height="16" viewBox="0 0 18 16"><path d="M1 8h15M10 2l6 6-6 6" fill="none" stroke="#fff" stroke-width="2"/></svg>
    </article>
    <article class="service-card card-3">
      <div class="service-photo" role="img" aria-label="Rocky cliffs above a glacier lake"></div>
      <div class="service-text"><h3 class="service-name">Transparent Fees</h3><p class="service-desc">You'll always know what you pay and how we get paid</p></div>
      <svg class="service-arrow" width="18" height="16" viewBox="0 0 18 16"><path d="M1 8h15M10 2l6 6-6 6" fill="none" stroke="#fff" stroke-width="2"/></svg>
    </article>
    <article class="service-card card-4">
      <div class="service-photo" role="img" aria-label="Colourful stones under clear lake water"></div>
      <div class="service-text"><h3 class="service-name">We Give Back</h3><p class="service-desc">We support and better our local communities</p></div>
      <svg class="service-arrow" width="18" height="16" viewBox="0 0 18 16"><path d="M1 8h15M10 2l6 6-6 6" fill="none" stroke="#fff" stroke-width="2"/></svg>
    </article>
  </div>
</body>
</html>
```